New Business Card Design Project for Handyman Business

I would like to purchase a customized version of a design you have previously submitted - https://www.plimvaro.example/work/58302716
I love this design!
I am hoping you can design something similar to this for our Handyman Business.
Attached is our logo and some graphics we have used.
Here is a link to the Google Doc with the content that needs to be included, https://files.trenowick.example/sheet/q/4XRKW-7hLp2DnQv8sTc5ma-ZzoeB3kWu9YyTgp6HJ__RmwNdVcQeLbs4jfnv0ztqxhaK7M41p9ggWHe/view
Target Market(s)
Real Estate Agents, Home Owners and Property Managers
Industry/Entity Type
Construction/ Speciality Trade
Contact Information for Business Card
https://files.trenowick.example/sheet/7QpaRzN_ukoyb4cXTwLHhJe8KnuSbPjCr2QDaLy6nwod/view?mode=shared
Font styles to use
Other font styles liked:
- Ubuntu
Look and feel
Each slider illustrates characteristics of the customer's brand and the style your logo design should communicate.

```html
<!DOCTYPE html>
<html lang="en">
<head>
<meta charset="utf-8">
<title>Tidycraft Business Card</title>
<link href="https://fonts.googleapis.com/css2?family=Ubuntu:wght@400;500;700&display=swap" rel="stylesheet">
<style>
  :root {
    --backdrop: #959595;
    --card-white: #ffffff;
    --brand-blue: #2b78c2;
    --brand-blue-deep: #2272bd;
    --pattern-blue: #3383cb;
    --brand-green: #4cb848;
    --brand-orange: #ea6a3d;
    --text-grey: #777777;
  }
  * { margin: 0; padding: 0; box-sizing: border-box; }
  html, body { width: 1200px; height: 1000px; overflow: hidden; }
  body {
    background: var(--backdrop);
    font-family: "Ubuntu", sans-serif;
    position: relative;
  }
  .card {
    position: absolute;
    width: 349px;
    height: 597px;
    border-radius: 22px;
    overflow: hidden;
  }
  .card-front { left: 195px; top: 199px; background: var(--card-white); }
  .card-back { left: 640px; top: 200px; background: var(--brand-blue-deep); }

  .center-line {
    position: absolute;
    left: 0; width: 100%;
    text-align: center;
    white-space: nowrap;
  }

  /* Front */
  .brand-mark {
    position: absolute;
    left: 160px; top: 46px;
    width: 30px; height: 30px;
    background: var(--brand-green);
    border-radius: 4px;
  }
  .brand-name-front {
    top: 100px;
    font-size: 38px;
    font-weight: 500;
    color: var(--brand-blue);
    letter-spacing: -0.5px;
  }
  .tagline-front {
    top: 144px;
    font-size: 11.5px;
    font-weight: 500;
    letter-spacing: 1.4px;
    color: var(--brand-orange);
  }
  .portrait {
    position: absolute;
    left: 98px; top: 177px;
    width: 154px; height: 154px;
    border-radius: 50%;
    background: radial-gradient(circle at 50% 45%, #d9a48a 0%, #c58a6e 30%, var(--brand-orange) 62%);
  }
  .person-name {
    top: 350px;
    font-size: 18px;
    font-weight: 500;
    letter-spacing: 1px;
    color: var(--brand-blue);
  }
  .person-role {
    top: 373px;
    font-size: 14px;
    color: var(--brand-orange);
  }
  .contact-icons {
    position: absolute;
    left: 0; top: 404px;
  }
  .contact-list {
    top: 450px;
    font-size: 17px;
    line-height: 22px;
    color: var(--text-grey);
  }
  .services {
    top: 541px;
    font-size: 16px;
    line-height: 21px;
    color: var(--brand-orange);
  }
  .service-dot {
    display: inline-block;
    width: 8px; height: 8px;
    border-radius: 50%;
    background: var(--brand-green);
    margin: 0 3px 2px;
    vertical-align: middle;
  }

  /* Back */
  .back-pattern {
    position: absolute;
    inset: 0;
    background: linear-gradient(180deg, var(--pattern-blue) 0%, var(--brand-blue-deep) 100%);
  }
  .brand-mark-back {
    position: absolute;
    left: 214px; top: 337px;
    width: 24px; height: 24px;
    background: var(--card-white);
    border-radius: 3px;
  }
  .brand-name-back {
    top: 425px;
    font-size: 42px;
    font-weight: 500;
    color: var(--card-white);
    letter-spacing: -0.5px;
  }
  .tagline-back {
    top: 473px;
    font-size: 12.5px;
    font-weight: 500;
    letter-spacing: 2px;
    color: var(--brand-orange);
  }
  .social-row {
    position: absolute;
    left: 0; top: 498px;
  }
  .hashtag {
    top: 540px;
    font-size: 16px;
    color: var(--card-white);
  }
</style>
</head>
<body>

<section class="card card-front">
  <div class="brand-mark"></div>
  <div class="center-line brand-name-front">tidycraft</div>
  <div class="center-line tagline-front">HOME CARE SPECIALISTS</div>

  <div class="portrait" role="img" aria-label="Portrait photo of the owner on an orange circle"></div>

  <div class="center-line person-name">MORGAN HALE</div>
  <div class="center-line person-role">Owner/ Handyman</div>

  <svg class="contact-icons" width="349" height="36" viewBox="0 0 349 36">
    <g stroke="var(--brand-green)" stroke-width="2" fill="none">
      <line x1="77" y1="18" x2="115" y2="18"/>
      <line x1="233" y1="18" x2="272" y2="18"/>
      <circle cx="137" cy="18" r="16"/>
      <circle cx="174" cy="18" r="16"/>
      <circle cx="210" cy="18" r="16"/>
    </g>
    <path fill="var(--brand-blue)" d="M131 10c1-1 2-1 3 0l2 3c.5 1 0 1.6-.7 2.2l-.8.7c.8 1.8 2.2 3.3 4 4.2l.8-.8c.6-.6 1.3-1 2.1-.5l3 2c1 .7 1 1.7 0 2.6l-1.3 1.2c-1.3 1.2-4.7.3-7.8-2.8s-4.2-6.5-3-7.8z"/>
    <g>
      <rect x="165" y="12" width="18" height="12" rx="1" fill="var(--brand-blue)"/>
      <polyline points="165.5,12.5 174,19 182.5,12.5" fill="none" stroke="#fff" stroke-width="1.4"/>
    </g>
    <g fill="none" stroke="var(--brand-blue)" stroke-width="1.6">
      <circle cx="210" cy="18" r="8"/>
      <ellipse cx="210" cy="18" rx="3.5" ry="8"/>
      <line x1="202" y1="18" x2="218" y2="18"/>
      <path d="M203.5 13.5h13M203.5 22.5h13"/>
    </g>
  </svg>

  <div class="center-line contact-list">
    (555) 014-2297<br>
    morgan@tidycraft-pro.example<br>
    Tidycraft-pro.example
  </div>

  <div class="center-line services">
    Commercial and Resdiential Handyman<br>
    Improve<span class="service-dot"></span>Repair<span class="service-dot"></span>Remodel<span class="service-dot"></span>Maintain
  </div>
</section>

<section class="card card-back">
  <div class="back-pattern" role="img" aria-label="Repeating brand pattern in soft blue tones"></div>
  <div class="brand-mark-back"></div>
  <div class="center-line brand-name-back">tidycraft</div>
  <div class="center-line tagline-back">HOME CARE SPECIALISTS</div>

  <svg class="social-row" width="349" height="36" viewBox="0 0 349 36">
    <g stroke="var(--card-white)" stroke-width="2" fill="none">
      <line x1="50" y1="18" x2="88" y2="18"/>
      <line x1="260" y1="18" x2="298" y2="18"/>
      <circle cx="114" cy="18" r="16"/>
      <circle cx="155" cy="18" r="16"/>
      <circle cx="196" cy="18" r="16"/>
      <circle cx="237" cy="18" r="16"/>
    </g>
  </svg>

  <div class="center-line hashtag">#tidycraftHandymanServices</div>
</section>

</body>
</html>
```